Simple but elegant business card/logo design for exclusive beauty business

We need a logo designed for a new elegant and exclusive beauty business called "R". The logo itself should be a stylistic and custom design for the letter "R". We would like the business card to have the logo as the centrepiece on a clean background. Gold Logo on black background or silver on white background.

The business card details should be displayed centre of the card. Details are as follows:

Tamsin Earle
Facebook: /shinesoftlyr
Instagram: /shinesoftlyr

The words "Shine Softly" should also appear somewhere on the card.

Industry/Entity Type

Business

Logo Text

G

Requirements
Must have
• Design must be simple, clean and elegant
Should not have
• The design should not be cluttered

```html
<!DOCTYPE html>
<html lang="en">
<head>
<meta charset="utf-8">
<title>Tamsin Earle — Business Card</title>
<link rel="stylesheet" href="https://fonts.googleapis.com/css2?family=Jost:wght@200;400&display=swap">
<style>
  :root {
    --card-black: #000000;
    --gold: #d9a325;
    --gold-light: #e8b838;
  }
  html, body {
    margin: 0;
    padding: 0;
    width: 1200px;
    height: 774px;
    overflow: hidden;
    background: var(--card-black);
  }
  .card {
    position: relative;
    width: 1200px;
    height: 774px;
    background: var(--card-black);
    font-family: "Jost", "Helvetica Neue", Arial, sans-serif;
    color: var(--gold);
  }
  .card__name {
    position: absolute;
    left: 0;
    right: 0;
    top: 212px;
    margin: 0;
    text-align: center;
    font-weight: 400;
    font-size: 96px;
    line-height: 1;
    letter-spacing: 3px;
    text-transform: uppercase;
    color: var(--gold-light);
  }
  .contact {
    position: absolute;
    left: 352px;
    width: 520px;
    height: 60px;
    display: flex;
    align-items: center;
  }
  .contact--first { top: 392px; }
  .contact--second { top: 482px; }
  .contact__marker {
    width: 58px;
    height: 58px;
    flex: none;
  }
  .contact__marker circle {
    fill: none;
    stroke: var(--gold);
    stroke-width: 3;
  }
  .contact__handle {
    margin-left: 98px;
    font-weight: 200;
    font-size: 60px;
    line-height: 1;
    letter-spacing: 3px;
    color: var(--gold);
  }
</style>
</head>
<body>
  <main class="card">
    <h1 class="card__name">Tamsin Earle</h1>

    <div class="contact contact--first">
      <svg class="contact__marker" viewBox="0 0 58 58" aria-hidden="true">
        <circle cx="29" cy="29" r="26"/>
      </svg>
      <span class="contact__handle">shinesoftlyr</span>
    </div>

    <div class="contact contact--second">
      <svg class="contact__marker" viewBox="0 0 58 58" aria-hidden="true">
        <circle cx="29" cy="29" r="26"/>
      </svg>
      <span class="contact__handle">shinesoftlyr</span>
    </div>
  </main>
</body>
</html>
```